We need a web design for our business in which we provide complete network packages.

Hello Designers!

First, we’d like to make clear that rather than simple web design contents. We want someone that can help design our visual branding, help us communicate a sentiment. And we are willing to pay for that.

Who are we?

We are Harbor Lumen. Our company is based in Rotterdam, the Netherlands. We are providing a unique full-service concept for (wireless) communication networks within small to mid-range businesses. This means we will not only provide the hardware needed for a fast and secure network within a company, but will also install, optimize, support and maintain it. 

Harbor Lumen is a new brand of a company called Vector Lumen which has over 15 years of experience in the market of customer service and support. Harbor Lumen is the first satellite of more to come. Like Gear Lumen and others Planets, all have a focus on full service solutions.

Harbor Lumen has an experienced support center from which we can monitor our clients network in real time. Our clients don’t have to worry about anything, if something is not working correctly, we will fix it pro actively. Our clients range from education and training facilities, catering, industry, logistics, health care, consultancy agencies and high end consumers. 

In an overview all Unique Selling Points of Harbor Lumen:
• Professional service, both on location and remote!
• Direct clear price indication via our unique business configuration wizard
• A specific and complete quotation after a personal intake, within two days.
• Backed by a professional call center open 12 hours a day and open on Saturdays as well.
• Backed by a professional repair center with more than 15 years of experience.
• Installation and configuration included.
• Optimization included within the first three months powered by AI and machine learning.
• Real time remote maintenance. Quality control, security and interference.

Logo
For our business we need a logo. The logo needs to tell what we stand for and what we do. It will be used in both online and offline communication to our customers. Mainly e-mail and digital forms. As Harbor Lumen is one of the branches within our company we would like the logo to be part of a series in the future, which should be recognizable as part of a group of websites/brands.

Website
For our business we need a website.  The website needs a story and matching design and this is where you come in. The main focus of this website is to provide information, but more importantly to guide the user to our special quotation business configuration wizard. This business configuration wizard allows users to fill in information about their business and wish requirements, at which they will receive a real time price indication on completion. 

Configuration wizard
This business configuration wizard is developed separately by our own development team but should be part of the website in look and feel.. Our development team will develop the business configuration wizard and embed it in the website. 
The setup of the website should be focused on leading all visitors to the business configuration wizard which we create our quality leads. The website will inform the possible customers/leads on the unique selling points and then remind the customer to use the business configuration wizard to get a direct price indication. 

For the website and logo we need the whole package, the design you are creating needs to have returning elements like fonts, icons, color use,  images, maybe even characters etc. You name it! 
There needs to be a common thread in the design so we can reuse elements in, for example, the email templates, the work order or receipt we give to our customers (we may contact the winner of the contest to design these for us as well!). 

The layout needs to be complete. We want something modern. A one page design that is bright and colorful with collapsing area’s to show more information. 

Website wishes and requirements
The process:
The main function of our website, besides giving a clear indication what we do, will be to guide the user to our ‘business configuration wizard’. 

Website functionality:
Our website will be our main form of communication. We need a main/front page designed in a long single scrolling page style. Users can click on buttons to view more information. Information that was hidden before. We have included our own temporary mock ups to give you an idea of the flow we desire for the website. The titles and headers in these mock ups are in Dutch but we will translate this in the description below. These mock ups are just that, an idea about the visual presentation. You are free to implement your own design, fonts, icons, pictures etc.

The page will have 6 different areas (beside the top ‘hero’ part) and a final 7th area which is the “end page” and is a big business configuration wizard promotion.In each area you are pointed towards the business configuration wizard but if you scroll all the way down you will end up with this 7th area which is all about the wizard. However these 6 areas will need to be ‘expandable/collapsible’, meaning the user can click a “read more” button at which the element will expand to show extra information beneath it. The user can then collapse this element again by closing the part that just opened.

1. Top/Hero - Customers will be able to configure their own price indication through our wizard. So there will need to be a prominent button at the top of our main page and on the 7th area that will bring the customer to this wizard/application. This will need to be a focus throughout the whole website, meaning this button is a returning element. Furthermore the top needs two menus. One for navigating the main page itself, the other one is for switching between the different industry ‘flavors’ (Education, Logistics, Health Care etc). The idea is that the photos and text on the website will change depending on the industry picked. The design and layout remains the same however. The mock ups are based on ‘education’ and another based on logistics.

2. Real time Maintenance (Beheer) – This will be a collapsible component. It will provide a brief description of our maintenance service. The ‘configure now!’ button will need to be displayed in this area as well. This component is collapsible, meaning the user can click on a ‘Read more’ (Dutch: lees meer) button at which the element will open up to show extra information (2.1).
2.1 The extra information that can be collapsed by clicking the ‘X’ button. The headers on this page read “Carefree real time maintenance”, “Certified team of administrators”, “High service level”, “Defects immediately detected”, “Continuous remote maintenance”.

3.  Service range (Bereik) - This will be a collapsible component. It will provide a brief description of how we provide for enough wifi range within a building or company. The ‘configure now!’ button will need to be displayed in this area as well. This component is collapsible, meaning the user can click on a ‘Read more’ (Dutch: lees meer) button at which the element will open up to show extra information (3.1).
3.1 The extra information that can be collapsed by clicking the ‘X’ button. The headers on this page read “Enough range everywhere”, “Machine learning for maximum range”, “Different types of access points”, “Beamforming & Mu-MiMo”, “Multiple locations connected”.

4. Speed (Snelheid) -  This is the only component that needs to collapse twice. It will provide a brief description of how we will guarantee the fastest network speed possible. The ‘configure now!’ button will need to be displayed in this area as well. This component is collapsible, meaning the user can click on a ‘Read more’ (Dutch: lees meer) button at which the element will open up to show extra information (4.1).
4.1 The extra information that can be collapsed by clicking the ‘X’ button. The headers on this page read “Band steering, “Airtime fairness”, “Load balancing”. The user will be able to open up another element to show even more information (4.2).
4.2 This will mainly show the diagrams shown in the mock ups. It will provide extra information on what is meant by “Airtime fairness” and “Load balancing”.

5.  Manageable Costs (Beheersbare kosten) - This will be a collapsible component. It will provide a brief description of how users can manage their own costs. The ‘configure now!’ button will need to be displayed in this area as well. This component is collapsible, meaning the user can click on a ‘Read more’ (Dutch: lees meer) button at which the element will open up to show extra information (5.1).
5.1 The extra information that can be collapsed by clicking the ‘X’ button. The headers on this page read “Manageable costs”, “Upfront insight in predicated costs”, “Best price/quality ratio”, “10 years of warranty”, “High availability”.

6.  Protected and secure (Beschermd en veilig) -  This will be a collapsible component. It will provide a brief description of our protection and security guaranties. The ‘configure now!’ button will need to be displayed in this area as well. This component is collapsible, meaning the user can click on a ‘Read more’ (Dutch: lees meer) button at which the element will open up to show extra information (6.1).
6.1 The extra information that can be collapsed by clicking the ‘X’ button. The headers on this page read “Protected and Secure”, “Protected by Kelvo”, “Fire resistant and dust free”, “Managed and maintained in the Netherlands”.

7. Extras (Extra’s) - This will be a collapsible component. It will provide a brief description of additional options which our solution can provide. The ‘configure now!’ button will need to be displayed in this area as well. This component is collapsible, meaning the user can click on a ‘Read more’ (Dutch: lees meer) button at which the element will open up to show extra information (7.1).
7.1 The extra information that can be collapsed by clicking the ‘X’ button. The headers on this page read “Connection with portals like Chatloom”, “Everything in one cable”, “Cloud ready”, “Ready for even more?”.

8. unique business configuration wizard - This is the final page to (once again!) push the visitor to the ‘configure now!’ button showing some reasons to click right now.

For now, we need a logo and a website designed. We would also like a design for the configuration wizard in the same style as the website.

What we'd like:
- A modern professional, but fun, appearance
- Elements like icons to have a flat design.
- Website can be used for the different industry flavors (for example, our mockups are geared towards clients in the education sector, but we can simply swap some of the photos and content to reflect the health care sector).
- Keep in mind that the website will need to be responsive when designing!
- Create a fun and trustworthy feeling.

We will be able to provide stock photographs if necessary!

```html
<!DOCTYPE html>
<html lang="en">
<head>
<meta charset="utf-8">
<title>Harbor Lumen – Configuration Wizard</title>
<link href="https://fonts.googleapis.com/css2?family=Quicksand:wght@400;500;600;700&display=swap" rel="stylesheet">
<style>
  :root{
    --red:#e8262a;
    --ink:#141414;
    --muted:#6b6b6b;
    --stage:#6a6a6a;
    --paper-top:#f3f0eb;
    --paper-bottom:#e8e1da;
    --white:#ffffff;
    --card:#f4f1ed;
    --line:#d9d4ce;
  }
  *{box-sizing:border-box;margin:0;padding:0}
  html,body{width:701px;height:1200px;overflow:hidden}
  body{background:var(--stage);font-family:"Quicksand",sans-serif;color:var(--ink);position:relative}
  .screen{position:absolute;left:19px;width:663px;height:373px;
    background:linear-gradient(180deg,var(--paper-top),var(--paper-bottom));
    box-shadow:0 2px 6px rgba(0,0,0,.35);overflow:hidden}
  .screen--estimate{top:21px}
  .screen--areas{top:413px}
  .screen--delete{top:806px}
  .sidebar{position:absolute;left:0;top:0;width:115px;height:100%;background:var(--white)}
  .brand{position:absolute;left:18px;top:26px;font-weight:700;font-size:17px;line-height:18px;color:var(--ink);letter-spacing:-.2px}
  .brand-dot{display:inline-block;width:6px;height:6px;border-radius:50%;background:var(--red);margin-left:3px;vertical-align:middle}
  .step{position:absolute;left:106px;width:18px;height:18px;border-radius:50%;font-weight:700;font-size:12px;display:flex;align-items:center;justify-content:center}
  .step--done{background:var(--red)}
  .step--current{background:var(--white);border:2px solid var(--red);color:var(--ink);left:105px;width:20px;height:20px}
  .step--next{background:var(--white);box-shadow:0 0 2px rgba(0,0,0,.4);color:var(--ink)}
  .abs{position:absolute;white-space:nowrap}
  .wrap{white-space:normal}
  .cost-label{font-weight:700;font-size:12.5px;color:var(--red)}
  .cost-value{font-weight:700;font-size:12.5px;color:var(--red);width:80px;text-align:right}
  .cost-items{font-size:6.8px;color:var(--muted);line-height:8.4px}
  .total{font-weight:700;font-size:15.5px;color:var(--ink)}
  .note{font-size:9px;color:var(--muted);line-height:10.8px}
  .field-label{font-weight:700;font-size:10.5px}
  .field{height:13px;width:169px;background:var(--white);border-radius:3px;font-size:7.5px;padding:2px 3px;color:#333}
  .check{width:15px;height:15px;border-radius:3px;background:var(--white);border:1px solid var(--line)}
  .check-text{font-size:8.5px;color:#333}
  .btn{position:absolute;height:19px;border-radius:10px;font-weight:700;font-size:9px;display:flex;align-items:center;justify-content:center;gap:3px;white-space:nowrap}
  .btn--solid{background:var(--red);color:var(--white)}
  .btn--outline{border:1.5px solid var(--red);color:var(--red);background:transparent;font-size:9.3px}
  .intro{font-weight:700;font-size:8.4px}
  .area-photo{position:absolute;width:83px;height:63px;border-radius:9px}
  .photo-office{background:linear-gradient(160deg,#8d98a4,#4a5560 55%,#6f6a62)}
  .photo-canteen{background:linear-gradient(150deg,#c9a27a,#8c5634 45%,#3d2c25 80%,#6e7a6e)}
  .area-card{position:absolute;width:352px;height:63px;background:var(--card);border-radius:9px;box-shadow:0 1px 3px rgba(0,0,0,.18);padding:11px 14px;white-space:nowrap}
  .area-title{font-weight:700;font-size:15.5px;color:var(--red);line-height:18px}
  .area-title sup{font-size:8px}
  .area-type{font-weight:700;font-size:8.4px;line-height:10px;margin-top:1px}
  .area-users{font-size:8.4px;color:var(--muted);line-height:10px}
  .chevron{position:absolute;right:14px;top:22px}
  .remove{position:absolute;right:6px;top:17px;width:28px;height:28px;border-radius:50%;border:2.5px solid var(--ink);font-weight:700;font-size:13px;display:flex;align-items:center;justify-content:center}
</style>
</head>
<body>

<section class="screen screen--estimate">
  <aside class="sidebar"><div class="brand">Harbor<br>Lumen<span class="brand-dot"></span></div></aside>
  <div class="step step--done" style="top:138px"></div>
  <div class="step step--done" style="top:178px"></div>
  <div class="step step--current" style="top:217px">3</div>

  <div class="abs cost-label" style="left:204px;top:45px">hardware</div>
  <div class="abs cost-value" style="left:266px;top:45px">€ 385</div>
  <div class="abs cost-items" style="left:204px;top:60px">-switches<br>-Access points<br>-Cabling</div>
  <div class="abs cost-label" style="left:204px;top:86px">Installation</div>
  <div class="abs cost-value" style="left:266px;top:87px">€ 200</div>
  <div class="abs total" style="left:204px;top:104px">Estimate</div>
  <div class="abs total" style="left:246px;top:104px;width:100px;text-align:right">€ 585</div>

  <p class="abs note" style="left:204px;top:141px">This amount is excluding any taxes that may apply</p>
  <p class="abs note wrap" style="left:204px;top:162px;width:308px">This is a ball park estimate. Would you like a more fitting quote? Fill in your contact data below and we will contact you within one business day!</p>

  <div class="abs field-label" style="left:204px;top:197px">Company Name</div>
  <div class="abs field" style="left:204px;top:214px">Solvane</div>
  <div class="abs field-label" style="left:404px;top:196px">Your Name</div>
  <div class="abs field" style="left:404px;top:213px">Martin Keel</div>
  <div class="abs field-label" style="left:204px;top:237px">Phone Number</div>
  <div class="abs field" style="left:204px;top:253px">0600000000</div>
  <div class="abs field-label" style="left:404px;top:237px">E Mail</div>
  <div class="abs field" style="left:404px;top:253px">m.keel@solvane.test</div>

  <div class="abs check" style="left:403px;top:281px"></div>
  <div class="abs check-text" style="left:424px;top:283px">I give my permission to use my data</div>

  <div class="btn btn--solid" style="left:404px;top:312px;width:79px">
    <svg width="7" height="7" viewBox="0 0 10 10"><circle cx="5" cy="5" r="3.3" fill="none" stroke="#fff" stroke-width="2"/></svg>Modify</div>
  <div class="btn btn--solid" style="left:494px;top:312px;width:79px">
    <svg width="6" height="7" viewBox="0 0 8 10"><path d="M2 1 A4 4 0 0 1 2 9" fill="none" stroke="#fff" stroke-width="1.8"/></svg>Contact me</div>
</section>

<section class="screen screen--areas">
  <aside class="sidebar"><div class="brand">Harbor<br>Lumen<span class="brand-dot"></span></div></aside>
  <div class="step step--done" style="top:138px"></div>
  <div class="step step--current" style="top:176px">2</div>
  <div class="step step--next" style="top:217px">3</div>

  <div class="btn btn--outline" style="left:444px;top:42px;width:80px;height:20px">Add area +</div>
  <div class="btn btn--outline" style="left:533px;top:42px;width:80px;height:20px">Remove area ✖</div>

  <p class="abs intro" style="left:167px;top:107px">Describe your situation by adding all the area's (rooms, outdoors areas, etc.) where you want to offer Wi-Fi.</p>

  <div class="area-photo photo-office" style="left:168px;top:132px" role="img" aria-label="Photo of an open-plan office floor"></div>
  <div class="area-card" style="left:262px;top:132px">
    <div class="area-title">Office for about 75 people ( 500m<sup>2</sup> )</div>
    <div class="area-type">office without walls</div>
    <div class="area-users">max 20 heavy users who often concurrently use the internet</div>
    <svg class="chevron" width="9" height="18" viewBox="0 0 9 18"><path d="M1 1 L8 9 L1 17" fill="none" stroke="#141414" stroke-width="1.8"/></svg>
  </div>

  <div class="area-photo photo-canteen" style="left:168px;top:205px" role="img" aria-label="Photo of a canteen with tables and chairs"></div>
  <div class="area-card" style="left:262px;top:205px">
    <div class="area-title">Canteen first floor ( 50m<sup>2</sup> )</div>
    <div class="area-type">generic (open) space</div>
    <div class="area-users">max 20 heavy users who often concurrently use the internet</div>
    <svg class="chevron" width="9" height="18" viewBox="0 0 9 18"><path d="M1 1 L8 9 L1 17" fill="none" stroke="#141414" stroke-width="1.8"/></svg>
  </div>

  <div class="btn btn--solid" style="left:383px;top:312px;width:109px">&lt; Select scenario</div>
  <div class="btn btn--solid" style="left:503px;top:312px;width:109px">
    <svg width="13" height="11" viewBox="0 0 13 11"><path d="M0 0 H13 L6.5 11 Z" fill="#fff"/></svg>create WiFi solution</div>
</section>

<section class="screen screen--delete">
  <div class="btn btn--outline" style="left:371px;top:42px;width:80px;height:20px">Cancel ✖</div>
  <div class="btn btn--outline" style="left:460px;top:42px;width:92px;height:20px">Delete selection
    <svg width="5" height="7" viewBox="0 0 5 7"><rect x="0" y="0" width="5" height="1.2" fill="#e8262a"/><rect x="0.6" y="1.8" width="3.8" height="5.2" fill="#e8262a"/></svg></div>

  <p class="abs intro" style="left:109px;top:107px">Select the areas you want to delet</p>

  <div class="area-photo photo-office" style="left:109px;top:132px" role="img" aria-label="Photo of an open-plan office floor"></div>
  <div class="area-card" style="left:203px;top:132px">
    <div class="area-title">Office for about 75 people ( 500m<sup>2</sup> )</div>
    <div class="area-type">office without walls</div>
    <div class="area-users">max 20 heavy users who often concurrently use the internet</div>
    <div class="remove">X</div>
  </div>

  <div class="area-photo photo-canteen" style="left:109px;top:205px" role="img" aria-label="Photo of a canteen with tables and chairs"></div>
  <div class="area-card" style="left:203px;top:205px">
    <div class="area-title">Canteen first floor ( 50m<sup>2</sup> )</div>
    <div class="area-type">generic (open) space</div>
    <div class="area-users">max 20 heavy users who often concurrently use the internet</div>
    <div class="remove">X</div>
  </div>

  <div class="btn btn--solid" style="left:325px;top:312px;width:109px">&lt; Select scenario</div>
  <div class="btn btn--solid" style="left:445px;top:312px;width:109px">
    <svg width="13" height="11" viewBox="0 0 13 11"><path d="M0 0 H13 L6.5 11 Z" fill="#fff"/></svg>create WiFi solution</div>
</section>

</body>
</html>
```